Ashes of Quiet

I need for someone to create a book cover for a modern day Political Thriller. This book is along the lines of Gareth Pell or Ray Hudgens. Everyone in the book is in opposition. Hence the name. This cover will be for both ebook and physical book so I do not know if two individual pieces need to be done or not. Below is an excerpt to give you an idea about the main character

He knew he made the right decision as he changed his mind after speaking with the Director. No the real problem, thought Beckett is that in this business there are not any true friends and ultimately we all are going to die alone. It may be for your country, it may be over a mistake, it might even be over a woman or something you felt worth the sacrifice, even dumb ass luck. It was just that some day, he knew he was going to die. However, he knew two things, first tonight he was going to walk across the room and take that beautiful woman in his bed. Second, tomorrow he was going to kill anyone who did not give him the answers he wanted to hear. If they could not handle the unabashed truth, the hell with them and the Director both thought Beckett. Subterfuge is what got everyone to where they were at in the first place. Truth, Beckett decided would put them where they needed to be.

Target Market(s)

Anyone reading Political thrillers. Ages mid teen and up. Most of military would probably be interested in this book

Industry/Entity Type

Publishing

Font styles to use
Serif

Colors

Designer to choose colors to be used in the design.

Requirements
Must have
• The Designer will have total control of their design work. I will be choosing the one I think best. I'm open to all ideas
Nice to have
• attractive colors and scheme which are obviously eye catching.
Should not have
• no sexual puns, references or suggestions of any kind. This is a political thriller and will be advertised as such

```html
<!DOCTYPE html>
<html lang="en">
<head>
<meta charset="utf-8">
<title>Ashes of Quiet — R.J. Calloway</title>
<link href="https://fonts.googleapis.com/css2?family=Libre+Baskerville:wght@700&display=swap" rel="stylesheet">
<style>
  :root {
    --night: #060606;
    --haze: #2a2a2a;
    --stone-tan: #8d7d6c;
    --stone-mauve: #806d69;
    --stone-rose: #8a6f69;
    --stone-grey: #7b7775;
    --stone-teal: #5f716c;
    --pulse-green: #4fae5c;
    --flat-line: #7a4a4a;
    --query-grey: #8a8a8a;
    --author-tan: #8a7b6b;
  }
  html, body {
    margin: 0;
    padding: 0;
    width: 800px;
    height: 1200px;
    overflow: hidden;
    background: var(--night);
  }
  .cover {
    position: relative;
    width: 800px;
    height: 1200px;
    background: radial-gradient(ellipse 380px 520px at 400px 520px, var(--haze) 0%, #141414 55%, var(--night) 100%);
    overflow: hidden;
  }
  .cover-art {
    position: absolute;
    inset: 0;
    width: 800px;
    height: 1200px;
  }
  .serif-bold {
    font-family: "Libre Baskerville", Georgia, serif;
    font-weight: 700;
    text-anchor: middle;
  }
  .row-a { fill: var(--stone-tan); font-size: 175px; }
  .row-sh { fill: var(--stone-mauve); font-size: 128px; }
  .row-es { fill: var(--stone-rose); font-size: 128px; }
  .row-of { fill: var(--stone-grey); font-size: 86px; }
  .row-quiet { fill: var(--stone-teal); font-size: 142px; }
  .query-mark { fill: var(--query-grey); font-size: 130px; }
  .author-name { fill: var(--author-tan); font-size: 122px; }
</style>
</head>
<body>
<main class="cover">
  <svg class="cover-art" viewBox="0 0 800 1200" xmlns="http://www.w3.org/2000/svg">
    <defs>
      <radialGradient id="lamp-glow" cx="50%" cy="82%" r="60%">
        <stop offset="0%" stop-color="#ffffff" stop-opacity="0.9"/>
        <stop offset="35%" stop-color="#dcdcdc" stop-opacity="0.35"/>
        <stop offset="100%" stop-color="#ffffff" stop-opacity="0"/>
      </radialGradient>
      <linearGradient id="pulse-band" x1="0" y1="0" x2="0" y2="1">
        <stop offset="0%" stop-color="var(--pulse-green)" stop-opacity="0"/>
        <stop offset="50%" stop-color="var(--pulse-green)" stop-opacity="0.35"/>
        <stop offset="100%" stop-color="var(--pulse-green)" stop-opacity="0"/>
      </linearGradient>
    </defs>

    <rect class="lamp-area" x="340" y="0" width="100" height="230" fill="url(#lamp-glow)"
          role="img" aria-label="A bare lightbulb hanging on a cord, glowing"/>

    <g class="serif-bold">
      <text class="row-a" x="400" y="386" textLength="120" lengthAdjust="spacingAndGlyphs">A</text>
      <text class="row-sh" x="382" y="482" textLength="190" lengthAdjust="spacingAndGlyphs">SH</text>
      <text class="row-es" x="395" y="584" textLength="220" lengthAdjust="spacingAndGlyphs">ES</text>
      <text class="row-of" x="392" y="654" textLength="200" lengthAdjust="spacingAndGlyphs">OF</text>
      <text class="row-quiet" x="398" y="766" textLength="330" lengthAdjust="spacingAndGlyphs">QUIET</text>
    </g>

    <rect class="pulse-area" x="0" y="805" width="375" height="160" fill="url(#pulse-band)"
          role="img" aria-label="Green heartbeat monitor trace that flatlines"/>
    <line x1="420" y1="937" x2="800" y2="937" stroke="var(--flat-line)" stroke-width="2.5"/>
    <text class="serif-bold query-mark" x="398" y="936">?</text>

    <text class="serif-bold author-name" x="408" y="1105" textLength="680" lengthAdjust="spacingAndGlyphs">R.J. CALLOWAY</text>
  </svg>
</main>
</body>
</html>
```